Need Business Card Design, Letterhead and a Basic Form layout based on Existing Logo

We need (1) a business card design, (2) a letterhead design and (3) a basic form layout for an international holding company. This holding company has just formed two (2) sub-companies. The logo is the same for each company with only a simple word change for each company. The business card, letterhead and form design will be essentially the same for each company... with only the one word change being different.
The names of the companies are as follows:
1. Halvorn Trust Services
2. Halvorn Immigration Services
The design for the business card, letterhead and Form must be strong, clean and classy.
Our clients will be older, wealthy and mostly Asian. The design must project strength, stability and confidence.
The card may contain the following data:
1. The Logo
2. The name of the person
3. The title of the person
4. The address of the company
5. The Company Phone number
6. The personal mobile number
7. The Skype number (VOIP)
8. The WICKR number (IM)
9. The email
10. The website
We will attach AI files of our logo for the "Halvorn Trust Services" company in the colors Black/White and Blue in both Horizontal and Vertical format... We have also included separate files of the logo icon.
We uploaded the AI files to give the designer the maximum options regarding color and effects. We included the separate files for the icon because we would like to give the designer the option of a watermark. Also, we think it might be nice to highlight the icon on the back of the card perhaps with the website address.
We are not sure which colors or color combinations would be best for these two companies. We know the colors must again project strength, stability and confidence. Perhaps, a combination that might include Tan, Black and White... not sure... need design help... remember this has to have the presence of a bank-like institution... no cartoonish designs or flashy color combinations... please.
The basic form layout will be used for various questionaires, input sheets and instructions.... etc.
NOTE: The fonts used in the logo are Trajan Pro Bold for word "HALVORN" and Trajan Pro Regular for "XXXXXXXXX SERVICES".

```html
<!DOCTYPE html>
<html lang="en">
<head>
<meta charset="utf-8">
<title>Halvorn Trust Services – Business Card</title>
<link href="https://fonts.googleapis.com/css2?family=Cinzel:wght@400;700&family=Marcellus+SC&display=swap" rel="stylesheet">
<style>
  :root {
    --stage: #58595b;
    --ink: #000000;
    --paper: #ffffff;
    --soft-paper: #f2f2f2;
    --pattern-dark: #141414;
    --pattern-mid: #3c3c3c;
    --rule: #1a1a1a;
  }
  html, body {
    margin: 0;
    padding: 0;
    overflow: hidden;
  }
  .stage {
    position: relative;
    width: 1200px;
    height: 429px;
    background: var(--stage);
    overflow: hidden;
  }
  .card {
    position: absolute;
    overflow: hidden;
  }
  /* Front */
  .card--front {
    left: 71px;
    top: 71px;
    width: 511px;
    height: 294px;
  }
  .front-pattern {
    position: absolute;
    inset: 0;
    background: linear-gradient(135deg, var(--pattern-dark) 0%, var(--pattern-mid) 50%, var(--pattern-dark) 100%);
  }
  .front-badge {
    position: absolute;
    left: 125px;
    top: 103px;
    width: 250px;
    height: 87px;
    background: var(--ink);
    display: flex;
    align-items: center;
    justify-content: center;
    gap: 12px;
  }
  /* Back */
  .card--back {
    left: 607px;
    top: 67px;
    width: 514px;
    height: 300px;
    background: var(--paper);
  }
  .back-pattern {
    position: absolute;
    left: 0;
    right: 0;
    top: 93px;
    bottom: 0;
    background: linear-gradient(180deg, var(--soft-paper), var(--paper));
  }
  .back-header {
    position: absolute;
    left: 0;
    right: 0;
    top: 15px;
    height: 78px;
    background: var(--ink);
  }
  .back-header .brand {
    position: absolute;
    left: 22px;
    top: 17px;
    display: flex;
    align-items: center;
    gap: 14px;
  }
  .brand-square {
    width: 34px;
    height: 34px;
    background: var(--paper);
    flex: none;
  }
  .brand-text {
    color: var(--paper);
    font-family: "Cinzel", serif;
    line-height: 1;
  }
  .brand-name {
    font-weight: 700;
    font-size: 24px;
    letter-spacing: 0.5px;
    display: block;
  }
  .brand-tagline {
    font-weight: 400;
    font-size: 13px;
    display: block;
    margin-top: 2px;
    text-transform: none;
  }
  .holder {
    position: absolute;
    right: 20px;
    top: 20px;
    text-align: right;
    color: var(--paper);
    font-family: "Cinzel", serif;
    font-size: 17px;
    line-height: 21px;
    letter-spacing: 0.5px;
  }
  .contact {
    position: absolute;
    font-family: "Marcellus SC", serif;
    font-size: 15px;
    color: var(--ink);
    line-height: 30px;
    margin: 0;
  }
  .contact--left {
    left: 19px;
    top: 125px;
  }
  .contact--right {
    right: 20px;
    top: 125px;
    text-align: right;
  }
  .contact .address {
    line-height: 21px;
    display: block;
    margin-top: 4px;
  }
  .back-rule {
    position: absolute;
    left: 29px;
    width: 454px;
    top: 246px;
    height: 2px;
    background: var(--rule);
  }
  .website {
    position: absolute;
    left: 0;
    right: 0;
    top: 264px;
    text-align: center;
    font-family: "Cinzel", serif;
    font-weight: 700;
    font-size: 13px;
    letter-spacing: 0.5px;
    color: var(--ink);
  }
</style>
</head>
<body>
<main class="stage">

  <section class="card card--front" aria-label="Card front">
    <div class="front-pattern" role="img" aria-label="Bold black and white geometric maze pattern"></div>
    <div class="front-badge">
      <span class="brand-square"></span>
      <span class="brand-text">
        <span class="brand-name">HALVORN</span>
        <span class="brand-tagline">Trust Services</span>
      </span>
    </div>
  </section>

  <section class="card card--back" aria-label="Card back">
    <div class="back-pattern" role="img" aria-label="Faint light grey geometric maze pattern"></div>

    <header class="back-header">
      <div class="brand">
        <span class="brand-square"></span>
        <span class="brand-text">
          <span class="brand-name">HALVORN</span>
          <span class="brand-tagline">Trust Services</span>
        </span>
      </div>
      <div class="holder">
        <div class="holder-name">EDWIN CALLOWAY</div>
        <div class="holder-title">DIRECTOR</div>
      </div>
    </header>

    <p class="contact contact--left">
      T: 01632 960481<br>
      M: 0770 900412<br>
      VoIP: 0800555019
    </p>

    <p class="contact contact--right">
      IM: 0800555019<br>
      E: edwin.calloway@halvorn.com<br>
      <span class="address">27C Fenwick Avenue,<br>Lindford, Norfolkshire, NR21 4QB</span>
    </p>

    <div class="back-rule"></div>
    <div class="website">WWW.HALVORN.COM</div>
  </section>

</main>
</body>
</html>
```